Brisk Tide needs a web page for E-commerce site

Small startup business looking for a custom website for my New Saltwater apparel Co.

COMPANY OVERVIEW

Brisk Tide was founded In Mont Belvieu, Tx, right on the heart of pelican cove.

Brisk Tide is the adrenaline, sweat pumping moment you find yourself setting the hook on a monster fish. This is the moment when all your senses come to life as you work to land that trophy, and after a grueling fight when your hi-fiving your fishing buddies...It's that moment... when the waters and the air around you are Brisk Sweet....All or Nothing...pure Addiction......This is BRISK TIDE

Looking for a sharp clean sexy web page for my ecommerce page

I like the look of black background websites.

www.brisktidegear.example
Updates

I am using bigcommerce as my host site if that means anything to y'all

Thank you all for the submissions! There were some great ones!  I will have more projects in the future. thanks again

Target Market(s)

inshore/offshore fishing, saltwater enthusiast

Industry/Entity Type

Business

Requirements
Must have
• logo's

inshore/offshore fishing appeal

compatible with bigcommerce site

```html
<!DOCTYPE html>
<html lang="en">
<head>
<meta charset="utf-8">
<title>Brisk Tide – Shop</title>
<link rel="stylesheet" href="https://fonts.googleapis.com/css2?family=Open+Sans:wght@400;600;700;800&family=Roboto:wght@100;400;700&display=swap">
<style>
:root{
  --header-bg:#efefef;
  --body-bg:#181818;
  --body-bg-light:#242424;
  --ink:#1c1c1c;
  --muted:#3a3a3a;
  --red:#cd1a2d;
  --red-bright:#f0113f;
  --card-bg:#1b1b1b;
  --card-border:#3a3a3a;
  --footer-bg:#050505;
  --footer-text:#c9c9c9;
  --white:#ffffff;
}
*{box-sizing:border-box;margin:0;padding:0}
html,body{width:1200px;height:1027px;overflow:hidden}
body{position:relative;background:var(--body-bg);font-family:"Open Sans",Arial,sans-serif;color:var(--white)}
a{color:inherit;text-decoration:none}

/* Header */
.site-header{position:absolute;left:0;top:0;width:1200px;height:122px;background:linear-gradient(#f3f3f3,#e6e6e6)}
.brand{position:absolute;left:112px;top:38px;display:flex;align-items:center;gap:10px;font-family:"Open Sans",sans-serif;font-weight:800;font-size:40px;letter-spacing:1px;color:var(--ink)}
.brand-mark{width:14px;height:14px;background:currentColor;border-radius:50%}
.account-links{position:absolute;right:105px;top:12px;font-size:11px;color:var(--ink);word-spacing:1px}
.account-links span{margin:0 6px;color:var(--muted)}
.main-nav{position:absolute;top:83px;left:708px;display:flex;align-items:center;font-size:13px;color:#333}
.main-nav a{height:27px;line-height:27px}
.main-nav .is-active{background:var(--red);color:var(--white);font-weight:600;padding:0 10px;margin-right:49px}
.main-nav .nav-shipping{margin-right:63px}

/* Hero */
.hero-frame{position:absolute;left:112px;top:158px;width:970px;height:383px;border-radius:12px;background:linear-gradient(#3a3a3a,#0c0c0c 40%,#000);border:1px solid #4a4a4a;box-shadow:0 4px 14px rgba(0,0,0,.6)}
.hero-photo{position:absolute;left:13px;top:13px;width:944px;height:355px;background:linear-gradient(90deg,#1d5b62 0%,#26737a 38%,#3b2a2a 62%,#7a2344 80%,#4c1c2c 100%)}
.hero-title{position:absolute;left:35px;top:14px;font-family:"Roboto",sans-serif;font-weight:100;font-size:80px;color:var(--white);letter-spacing:-1px}

/* Categories */
.category-menu{position:absolute;left:109px;top:578px;width:199px;height:214px;background:var(--red);border-radius:8px;padding:0 8px;list-style:none}
.category-menu li{height:48px;line-height:48px;padding-left:8px;font-size:17px;border-bottom:1px solid rgba(0,0,0,.18)}
.category-menu li:first-child{height:61px;line-height:72px}
.category-menu li:last-child{border-bottom:none}

/* Products */
.product-card{position:absolute;top:579px;width:225px;height:213px;background:var(--card-bg);border:2px solid var(--card-border);border-radius:8px;font-family:Arial,Helvetica,sans-serif}
.product-card:nth-of-type(1){left:351px}
.product-card:nth-of-type(2){left:592px}
.product-card:nth-of-type(3){left:844px}
.product-photo{position:absolute;left:8px;top:8px;width:206px;height:136px}
.photo-dark{background:linear-gradient(#f0f0f0,#cfcfcf);box-shadow:inset 0 0 0 40px rgba(40,30,20,.0)}
.price-badge{position:absolute;right:1px;top:1px;width:58px;height:58px}
.price-badge text{font-family:"Roboto",sans-serif;font-weight:700;font-size:21px;fill:var(--white)}
.product-title{position:absolute;left:9px;top:152px;font-size:12.5px;font-weight:bold;color:#e6e6e6}
.product-text{position:absolute;left:10px;top:171px;width:196px;font-size:11px;line-height:14px;color:#e0e0e0;text-align:justify}
.more-info{position:absolute;right:15px;top:190px;font-size:11px;font-weight:bold;color:var(--red-bright)}

/* Footer */
.footer-band{position:absolute;left:0;top:866px;width:1200px;height:50px}
.site-footer{position:absolute;left:0;top:886px;width:1200px;height:141px;background:var(--footer-bg)}
.footer-brand{position:absolute;left:125px;top:62px;display:flex;align-items:center;gap:9px;font-weight:800;font-size:36px;color:var(--white)}
.footer-brand .brand-mark{width:12px;height:12px}
.footer-links{position:absolute;top:18px;list-style:none;font-size:11px;color:var(--footer-text);letter-spacing:.5px}
.footer-links li{height:22px;padding-left:17px;position:relative}
.footer-links li::before{content:"";position:absolute;left:2px;top:6px;width:5px;height:5px;border-radius:50%;background:#444}
.links-a{left:395px}.links-b{left:561px}.links-c{left:728px;top:22px}
.help-line{position:absolute;left:893px;top:22px;width:200px;text-align:center;font-family:Arial,Helvetica,sans-serif;font-weight:bold}
.help-label{font-size:11px;color:#cfcfcf;letter-spacing:1px}
.help-phone{font-size:13px;margin-top:5px}
.help-or{font-size:13px;margin-top:5px}
.help-online{font-size:11px;color:#bdbdbd;letter-spacing:.5px;margin-top:5px}
.help-email{font-size:13px;margin-top:7px}
</style>
</head>
<body>

<header class="site-header">
  <div class="brand"><span class="brand-mark"></span>BRISK TIDE</div>
  <nav class="account-links">
    <a href="#">My Account</a><span>|</span><a href="#">Order Status</a><span>|</span><a href="#">Wish Lists</a><span>|</span><a href="#">Gift Certificates</a><span>|</span><a href="#">View Cart</a><span>|</span><a href="#">Sign in or Create an account</a>
  </nav>
  <nav class="main-nav">
    <a href="#" class="is-active">Home</a>
    <a href="#" class="nav-shipping">Shipping &amp; Returns</a>
    <a href="#">RSS Syndication</a>
  </nav>
</header>

<section class="hero-frame">
  <div class="hero-photo" role="img" aria-label="Fashion photo of a model seated against a teal wall with butterflies"></div>
  <h1 class="hero-title">Shopping</h1>
</section>

<ul class="category-menu">
  <li>Ladies »</li>
  <li>Mens »</li>
  <li>Accessories</li>
  <li>Sale</li>
</ul>

<article class="product-card">
  <div class="product-photo" role="img" aria-label="Black t-shirt with printed graphic, front and back" style="background:linear-gradient(90deg,#ececec,#d9d9d9 20%,#2a2218 22%,#2a2218 78%,#d9d9d9 80%,#eaeaea)"></div>
  <svg class="price-badge" viewBox="0 0 58 58"><circle cx="29" cy="29" r="28" fill="#cd1a2d"/><text x="29" y="36" text-anchor="middle">$90</text></svg>
  <h2 class="product-title">Ipsum is simply dummy text</h2>
  <p class="product-text">Lorem Ipsum has been the industry's standard dummy</p>
  <a href="#" class="more-info">Moreinfo</a>
</article>

<article class="product-card">
  <div class="product-photo" role="img" aria-label="Yellow t-shirt with blue fish print, front and back" style="background:linear-gradient(90deg,#f2f2f2,#e3e3e3 12%,#f2ec99 18%,#f3ed9c 82%,#e3e3e3 88%,#f0f0f0)"></div>
  <svg class="price-badge" viewBox="0 0 58 58"><circle cx="29" cy="29" r="28" fill="#cd1a2d"/><text x="29" y="36" text-anchor="middle">$90</text></svg>
  <h2 class="product-title">Ipsum is simply dummy text</h2>
  <p class="product-text">Lorem Ipsum has been the industry's standard dummy</p>
  <a href="#" class="more-info">Moreinfo</a>
</article>

<article class="product-card">
  <div class="product-photo" role="img" aria-label="White t-shirt with teal fish print, front and back" style="background:linear-gradient(90deg,#dcdcdc,#c9c9c9 15%,#f7f7f7 22%,#ffffff 78%,#c9c9c9 85%,#dcdcdc)"></div>
  <svg class="price-badge" viewBox="0 0 58 58"><circle cx="29" cy="29" r="28" fill="#cd1a2d"/><text x="29" y="36" text-anchor="middle">$90</text></svg>
  <h2 class="product-title">Ipsum is simply dummy text</h2>
  <p class="product-text">Lorem Ipsum has been the industry's standard dummy</p>
  <a href="#" class="more-info">Moreinfo</a>
</article>

<footer class="site-footer">
  <div class="footer-brand"><span class="brand-mark"></span>BRISK TIDE</div>
  <ul class="footer-links links-a"><li>Who we are</li><li>In the press</li><li>Partners</li><li>Terms of service</li><li>Privacy policy</li></ul>
  <ul class="footer-links links-b"><li>Experts</li><li>Payments</li><li>Partner Program</li><li>Developers</li><li>Affiliates</li></ul>
  <ul class="footer-links links-c"><li>Features</li><li>Pricing</li><li>Showcase</li></ul>
  <div class="help-line">
    <div class="help-label">24/7 HELP LINE</div>
    <div class="help-phone">(555) 014 - 2290</div>
    <div class="help-or">OR</div>
    <div class="help-online">ONLINE HELP</div>
    <div class="help-email">help@brisktidegear.example</div>
  </div>
</footer>

<svg class="footer-band" viewBox="0 0 1200 50" preserveAspectRatio="none">
  <path d="M0 2 H172 L230 28 L288 2 H1200 V20 H290 L230 47 L170 20 H0 Z" fill="#f0113f"/>
</svg>

</body>
</html>
```